Webdesign für Blog zum Thema KINDERWUNSCH
Zielgruppe
Hallo, ich bin 41 Jahre alt und lebe mit meinem Mann und unseren beiden Kindern (und Hund Ki;)) in einem kleinen Ort im Rhein-Main-Gebiet.
Ich musste auf meine beiden Kinder jeweils lange warten und diese schwere Zeit habe ich nicht vergessen. Meine beste Freundin hat mich irgendwann dazu überredet, anderen Frauen, denen es ähnlich geht, zu helfen. Besonders kann ich mich daran erinnern, wie schwer es war, verlässliche, gut recherchierte Quellen zum Thema Kinderwunsch zu finden.
Zusammen mit meiner besten Freundin baue ich daher einen Blog auf, bei dem es genau um diese Themen gehen soll.
Zielgruppe:
• Frauen
• Mitte / Ende 30
• Verheiratet, keine Kinder
• Höheres Bildungsniveau / nicht zwingend Akademiker
Kernemotionen:
o grübelt / ist unsicher
o nimmt ungewollte Kinderlosigkeit persönlich
o ängstlich / teils verzweifelt
o ungeduldig
Aufgabenstellung
Es geht um das Design unseres Blogs.
Uns ist besonders wichtig, dass der Blog das Spannungsverhältnis Seriosität – Freude – Ruhe vermittelt.
Das Design soll folgendes transportieren:
• Seriös / glaubwürdig
• Hochwertig
• Sicherheit / Ruhe / Seelenfriede
• Hoffnung
• Positiv / herzlich / unbeschwert – aber dennoch ernsthaft
ZUM FARBKONZEPT ETC. SIEHE BITTE BRIEFING ANBEI

```html
<!DOCTYPE html>
<html lang="de">
<head>
<meta charset="utf-8">
<title>Über mich – Hoffnungsnest</title>
<link href="https://fonts.googleapis.com/css2?family=Asap:wght@400;500;700&display=swap" rel="stylesheet">
<style>
  :root {
    --teal: #5ab8c3;
    --teal-soft: #f3f9fa;
    --ink: #2e2e2e;
    --grey: #7a7a7a;
    --white: #ffffff;
    --photo-top: #9cc063;
    --photo-bottom: #c9d6a4;
  }
  * { margin: 0; padding: 0; box-sizing: border-box; }
  html, body { width: 1200px; height: 750px; overflow: hidden; background: var(--white); }
  body { font-family: "Asap", Arial, sans-serif; color: var(--ink); position: relative; }

  .page { position: absolute; left: 0; top: 0; width: 800px; height: 750px; overflow: hidden; }
  .top-stitch {
    position: absolute; left: 0; top: 0; width: 800px; height: 4px;
    background: repeating-linear-gradient(90deg, var(--teal) 0 7px, transparent 7px 10px);
  }
  .site-header { position: absolute; left: 0; top: 0; width: 800px; height: 129px; }
  .brand {
    position: absolute; left: 56px; top: 50px;
    display: flex; align-items: center; gap: 10px;
    font-size: 30px; font-weight: 400; color: var(--teal); letter-spacing: 0.2px;
  }
  .brand-dot { width: 40px; height: 40px; border-radius: 50%; background: var(--teal); }
  .main-nav { position: absolute; top: 66px; left: 524px; font-size: 13.5px; }
  .main-nav a { text-decoration: none; color: var(--grey); position: absolute; white-space: nowrap; }
  .main-nav a.current { color: var(--teal); font-weight: 700; }

  .page-intro {
    position: absolute; left: 0; top: 129px; width: 800px; height: 118px;
    background: var(--teal-soft); text-align: center;
  }
  .page-intro h1 { position: absolute; top: 26px; width: 100%; font-size: 28.5px; font-weight: 700; color: var(--teal); }
  .page-intro p { position: absolute; top: 68px; width: 100%; font-size: 15px; }

  .lead-quote {
    position: absolute; left: 110px; top: 300px; width: 565px;
    font-size: 15.2px; line-height: 18.3px;
  }
  .quote-mark { position: absolute; color: var(--teal); font-size: 42px; font-weight: 700; font-style: italic; line-height: 1; }
  .quote-open { left: 694px; top: 272px; }
  .quote-close { left: 66px; top: 376px; }

  .article-body {
    position: absolute; left: 68px; top: 419px; width: 647px;
    font-size: 12.3px; line-height: 18.3px; text-align: justify;
  }
  .article-body p + p { margin-top: 18.3px; }

  .portrait {
    position: absolute; left: 800px; top: 0; width: 400px; height: 750px;
    background: linear-gradient(180deg, var(--photo-top) 0%, var(--photo-bottom) 100%);
  }
</style>
</head>
<body>
  <div class="page">
    <div class="top-stitch"></div>
    <header class="site-header">
      <div class="brand"><span class="brand-dot"></span>Hoffnungsnest</div>
      <nav class="main-nav">
        <a href="#" style="left:0">Übersicht</a>
        <a href="#" class="current" style="left:84px">Über mich</a>
        <a href="#" style="left:173px">Kontakt</a>
      </nav>
    </header>

    <section class="page-intro">
      <h1>Über mich</h1>
      <p>Mein Weg zur Erfüllung meines Kinderwunsches.</p>
    </section>

    <span class="quote-mark quote-open">“</span>
    <blockquote class="lead-quote">Lorem ipsum dolor sit amet, consetetur sadipscing elitr, sed diam nonumy eirmod tempor invidunt ut labore et dolore magna aliquyam erat, sed diam voluptua. At vero eos et accusam et justo duo dolores et ea rebum. Stet clita kasd gubergren, no sea takimata sanctus est Lorem ipsum dolor sit amet.</blockquote>
    <span class="quote-mark quote-close">”</span>

    <article class="article-body">
      <p>Lorem ipsum dolor sit amet, consetetur sadipscing elitr, sed diam nonumy eirmod tempor invidunt ut labore et dolore magna aliquyam erat, sed diam voluptua. At vero eos et accusam et justo duo dolores et ea rebum. Stet clita kasd gubergren, no sea takimata sanctus est Lorem ipsum dolor sit amet. Lorem ipsum dolor sit amet, consetetur sadipscing elitr, sed diam nonumy eirmod tempor invidunt ut labore et dolore magna aliquyam erat, sed diam voluptua. At vero eos et accusam et justo duo dolores et ea rebum. Stet clita kasd gubergren, no sea takimata sanctus est Lorem ipsum dolor sit amet. Lorem ipsum dolor sit amet, consetetur sadipscing elitr, sed diam nonumy eirmod tempor invidunt ut labore et dolore magna aliquyam erat, sed diam voluptua. At vero eos et accusam et justo duo dolores et ea rebum. Stet clita kasd gubergren, no sea takimata sanctus est Lorem ipsum dolor sit amet.</p>
      <p>Duis autem vel eum iriure dolor in hendrerit in vulputate velit esse molestie consequat, vel illum dolore eu feugiat nulla facilisis at vero eros et accumsan et iusto odio dignissim qui blandit praesent luptatum zzril delenit augue duis dolore te feugait nulla facilisi. Lorem ipsum dolor sit amet, consectetuer adipiscing elit, sed diam nonummy nibh euismod tincidunt ut laoreet dolore magna aliquam erat volutpat.</p>
      <p>Ut wisi enim ad minim veniam, quis nostrud exerci tation ullamcorper suscipit lobortis nisl ut aliquip ex ea commodo consequat. Duis autem vel eum iriure dolor in hendrerit in vulputate velit esse molestie consequat, vel illum dolore eu feugiat nulla facilisis at vero eros et accumsan et iusto odio dignissim qui blandit praesent luptatum zzril delenit augue duis dolore te feugait nulla facilisi.</p>
    </article>
  </div>

  <div class="portrait" role="img" aria-label="Porträtfoto der Bloggerin vor sonnigem grünem Laub"></div>
</body>
</html>
```